quality electrical business needs a logo design

we need a logo design for our new company starting up. I'm a sole trader electrician. I want to make the PES prominent in Perant Electrical Services. Information I would want on the business card would be;
Business Name: Perant Electrical Services
What I do: Domestic/Commercial/Industrial Installation & Maintenance
Email Address: Bryce.perant@wavlo.net.au
Contact no: Bryce 0438261759
Electrical License no: EC57364

Open to different Colours but would like to see some with Navy blue. I want to promote professionalism and have a modern feel about it.

Industry/Entity Type

Electrical

```html
<!DOCTYPE html>
<html lang="en">
<head>
<meta charset="utf-8">
<title>Perant Electrical Services – Business Card</title>
<link rel="stylesheet" href="https://fonts.googleapis.com/css2?family=Michroma&family=Barlow+Semi+Condensed:wght@400;500&display=swap">
<style>
  :root {
    --navy: #0b1530;
    --lime: #a6c92a;
    --white: #ffffff;
    --backdrop: #9b9b9b;
    --ink: #0b1530;
  }
  * { box-sizing: border-box; margin: 0; padding: 0; }
  html, body {
    width: 1200px;
    height: 1000px;
    overflow: hidden;
    background: var(--backdrop);
  }
  .canvas {
    position: relative;
    width: 1200px;
    height: 1000px;
  }

  /* Business card */
  .card {
    position: absolute;
    left: 160px;
    top: 110px;
    width: 880px;
    height: 500px;
    background: var(--white);
    overflow: hidden;
    box-shadow: 0 6px 18px rgba(0,0,0,0.35);
  }
  .card__top {
    position: absolute;
    left: 0; top: 0;
    width: 100%;
    height: 300px;
    background: var(--navy);
  }
  .card__rule-white {
    position: absolute;
    left: 0; top: 282px;
    width: 100%;
    height: 2px;
    background: var(--white);
  }
  .card__rule-lime {
    position: absolute;
    left: 0; top: 318px;
    width: 100%;
    height: 3px;
    background: var(--lime);
  }
  .card__margin-line {
    position: absolute;
    left: 52px; top: 0;
    width: 2px;
    height: 100%;
    background: linear-gradient(to bottom, var(--white) 0 300px, var(--navy) 300px 100%);
  }

  .brand {
    position: absolute;
    left: 0; top: 36px;
    width: 100%;
    text-align: center;
    color: var(--white);
  }
  .brand__mark {
    font-family: "Barlow Semi Condensed", sans-serif;
    font-weight: 500;
    font-size: 82px;
    letter-spacing: 6px;
    line-height: 1;
  }
  .brand__name {
    margin-top: 34px;
    font-family: "Michroma", sans-serif;
    font-weight: 400;
    font-size: 34px;
    letter-spacing: 1px;
    line-height: 1;
  }
  .brand__services {
    margin-top: 18px;
    font-family: "Barlow Semi Condensed", sans-serif;
    font-size: 25px;
    color: var(--lime);
    line-height: 1;
  }

  .contact,
  .license {
    position: absolute;
    top: 370px;
    font-family: "Barlow Semi Condensed", sans-serif;
    font-size: 25px;
    line-height: 1.3;
    color: var(--ink);
  }
  .contact { left: 84px; }
  .license { left: 620px; }

  /* Logo variants */
  .logo-variant {
    position: absolute;
    top: 780px;
    font-family: "Barlow Semi Condensed", sans-serif;
    font-weight: 500;
    font-size: 96px;
    letter-spacing: 8px;
    line-height: 1;
  }
  .logo-variant--navy { left: 560px; color: var(--navy); }
  .logo-variant--white { left: 860px; color: var(--white); }
</style>
</head>
<body>
<main class="canvas">
  <section class="card" aria-label="Perant Electrical Services business card">
    <div class="card__top"></div>
    <div class="card__rule-white"></div>
    <div class="card__rule-lime"></div>
    <div class="card__margin-line"></div>

    <header class="brand">
      <div class="brand__mark">PES</div>
      <h1 class="brand__name">Perant Electrical Services</h1>
      <p class="brand__services">Domestic &bull; Commercial &bull; Industrial | Installation &amp; Maintenance</p>
    </header>

    <div class="contact">
      <p>Contact No: Bryce 0438261759</p>
      <p>e-mail: Bryce.perant@wavlo.net.au</p>
    </div>
    <div class="license">
      <p>Electrical License no:</p>
      <p>EC57364</p>
    </div>
  </section>

  <div class="logo-variant logo-variant--navy">PES</div>
  <div class="logo-variant logo-variant--white">PES</div>
</main>
</body>
</html>
```